Business card for Quorvane LLC | ||
Design a business card for a geospatial startup | ||
Use same font as used in my logo | ||
Cutting-Edge Corporate Modern Professional Simple |
Peter Hollis | ||
Chief Technical Officer | ||
48 Linden Row Suite 200 Bramwick, ST, 55821-3307 |
hello@quorvane-mail.net | ||
www.quorvane-site.net | ||
I''l provide the actual information once we get rolling :) I'd like to incorporate the corporate logo onto the card. Please keep the colors in the logo. You can use any font that looks good. |

```html
<!DOCTYPE html>
<html lang="en">
<head>
<meta charset="utf-8">
<title>Quorvane Stationery</title>
<link rel="stylesheet" href="https://fonts.googleapis.com/css2?family=Nunito+Sans:wght@400;600;700;800&display=swap">
<style>
  :root {
    --brand-blue: #2c4f93;
    --brand-green: #8cc63f;
    --ink: #4a4a4a;
    --muted: #8a8a8a;
    --paper: #ffffff;
    --backdrop: #2b2b2b;
  }
  * { margin: 0; padding: 0; box-sizing: border-box; }
  html, body { width: 1200px; height: 876px; overflow: hidden; background: var(--backdrop); }
  body { position: relative; font-family: "Nunito Sans", sans-serif; color: var(--ink); }

  .brand-name { font-family: "Nunito Sans", sans-serif; font-weight: 800; color: var(--brand-blue); letter-spacing: -0.5px; line-height: 1; }

  /* Letterhead */
  .letterhead { position: absolute; left: 67px; top: 101px; width: 497px; height: 715px; background: var(--paper); }
  .letterhead .brand-name { position: absolute; left: 22px; top: 30px; font-size: 32px; }
  .letterhead-contact { position: absolute; left: 380px; top: 20px; list-style: none; font-size: 7px; line-height: 10px; color: var(--muted); }
  .letterhead-contact li { position: relative; padding-left: 9px; }
  .letterhead-contact li::before { content: ""; position: absolute; left: 0; top: 3px; width: 5px; height: 5px; background: var(--brand-green); }
  .recipient { position: absolute; left: 22px; top: 160px; font-size: 8px; line-height: 11px; }
  .salutation { position: absolute; left: 22px; top: 212px; font-size: 8px; }
  .letter-body { position: absolute; left: 22px; top: 240px; width: 440px; font-size: 7.5px; line-height: 11px; color: var(--muted); }
  .letter-body p { margin-bottom: 11px; }
  .closing { position: absolute; left: 22px; top: 580px; font-size: 8px; line-height: 11px; }
  .signature { position: absolute; left: 30px; top: 620px; width: 70px; height: 26px; background: linear-gradient(90deg, #e8ecf4, #cfd7e8); }
  .letterhead-footer { position: absolute; left: 0; bottom: 0; width: 100%; height: 30px; background: var(--brand-blue); border-top: 3px solid var(--brand-green); color: #fff; font-size: 8px; letter-spacing: 2px; text-align: center; line-height: 27px; }

  /* Business card */
  .business-card { position: absolute; left: 590px; top: 101px; width: 574px; height: 264px; background: var(--paper); border-radius: 8px; overflow: hidden; }
  .business-card .brand-name { position: absolute; left: 0; width: 100%; text-align: center; top: 50px; font-size: 40px; }
  .card-band { position: absolute; left: 0; bottom: 0; width: 100%; height: 128px; background: var(--brand-blue); border-top: 4px solid var(--brand-green); color: #fff; }
  .card-identity { position: absolute; left: 40px; top: 34px; }
  .card-name { font-size: 24px; font-weight: 700; }
  .card-title { font-size: 10px; margin-top: 4px; }
  .card-divider { position: absolute; left: 298px; top: 22px; width: 1px; height: 80px; background: rgba(255,255,255,0.6); }
  .card-contact { position: absolute; left: 314px; top: 26px; list-style: none; font-size: 8.5px; line-height: 17px; }
  .card-contact li { display: flex; align-items: center; gap: 6px; }
  .card-contact svg { width: 9px; height: 9px; fill: #fff; }

  /* Envelopes */
  .envelope { position: absolute; left: 590px; width: 574px; height: 216px; background: var(--paper); }
  .envelope-back { top: 384px; }
  .envelope-back svg { position: absolute; inset: 0; }
  .envelope-back .flap-name { position: absolute; left: 0; width: 100%; text-align: center; top: 32px; font-size: 26px; color: #fff; }
  .envelope-back .seal-name { position: absolute; left: 0; width: 100%; text-align: center; top: 136px; font-size: 28px; }
  .envelope-front { top: 629px; }
  .envelope-front .brand-name { position: absolute; left: 0; width: 100%; text-align: center; top: 72px; font-size: 44px; }
  .envelope-footer { position: absolute; left: 0; bottom: 0; width: 100%; height: 28px; background: var(--brand-blue); border-top: 3px solid var(--brand-green); color: #fff; font-size: 8px; line-height: 25px; padding-left: 12px; }
</style>
</head>
<body>

<section class="letterhead">
  <div class="brand-name">Quorvane</div>
  <ul class="letterhead-contact">
    <li>48 Linden Row</li>
    <li>Suite 200</li>
    <li>Bramwick, ST, 55821-3307</li>
    <li>(800) 555-0147</li>
  </ul>
  <div class="recipient">Marla Fenwick<br>12 Ashgrove Lane<br>Kellerton</div>
  <div class="salutation">Dear Marla Fenwick,</div>
  <div class="letter-body">
    <p>Thank you for meeting with our team last week to discuss your mapping needs. We have prepared an outline of how our tracking platform can support your field operations, reduce reporting delays and give your managers a clear view of every asset in real time.</p>
    <p>Our location engine combines satellite, cellular and sensor data into a single live map. Each vehicle, device or shipment is shown with its current position, recent route and status, so that dispatchers can respond quickly when plans change during the day.</p>
    <p>Setup is simple. Our engineers will connect your existing systems, import your current fleet records and train your staff on the dashboard. Most clients are fully running within two weeks, with ongoing support available from our office at any hour.</p>
    <p>Please find the full proposal and pricing enclosed. We would welcome the chance to answer any questions and look forward to working together on the next stage of your project.</p>
  </div>
  <div class="closing">Yours Sincerely<br>Owen Treloar</div>
  <div class="signature" role="img" aria-label="Handwritten signature"></div>
  <div class="letterhead-footer">www.quorvane-site.net</div>
</section>

<section class="business-card">
  <div class="brand-name">Quorvane</div>
  <div class="card-band">
    <div class="card-identity">
      <div class="card-name">Peter Hollis</div>
      <div class="card-title">Chief Technical Officer</div>
    </div>
    <div class="card-divider"></div>
    <ul class="card-contact">
      <li><svg viewBox="0 0 10 10"><path d="M5 0a3.5 3.5 0 0 0-3.5 3.5C1.5 6 5 10 5 10s3.5-4 3.5-6.5A3.5 3.5 0 0 0 5 0zm0 5a1.5 1.5 0 1 1 0-3 1.5 1.5 0 0 1 0 3z"/></svg>48 Linden Row, Suite 200, Bramwick, ST, 55821-3307</li>
      <li><svg viewBox="0 0 10 10"><path d="M2 0l2 2.5-1 1.2a6 6 0 0 0 3.3 3.3l1.2-1L10 8l-1.5 2C4 10 0 6 0 1.5z"/></svg>(800) 555-0147</li>
      <li><svg viewBox="0 0 10 10"><path d="M0 2h10v6H0zm1 1v.3l4 2.5 4-2.5V3z"/></svg>hello@quorvane-mail.net</li>
      <li><svg viewBox="0 0 10 10"><circle cx="5" cy="5" r="4.5"/></svg>www.quorvane-site.net</li>
    </ul>
  </div>
</section>

<section class="envelope envelope-back">
  <svg viewBox="0 0 574 216" width="574" height="216">
    <polyline points="0,40 287,122 574,40" fill="none" stroke="#c9c9c9" stroke-width="1.5"/>
    <polyline points="0,216 250,118 324,118 574,216" fill="none" stroke="#e0e0e0" stroke-width="1"/>
    <polygon points="0,0 574,0 574,22 287,94 0,22" fill="var(--brand-blue)"/>
    <polyline points="0,22 287,94 574,22" fill="none" stroke="var(--brand-green)" stroke-width="3"/>
  </svg>
  <div class="brand-name flap-name">Quorvane</div>
  <div class="brand-name seal-name">Quorvane</div>
</section>

<section class="envelope envelope-front">
  <div class="brand-name">Quorvane</div>
  <div class="envelope-footer">48 Linden Row, Suite 200, Bramwick, ST, 55821-3307</div>
</section>

</body>
</html>
```